Create a memorable Web Design for real estate branding

we are a Minnepolis brokerage and boutique housing specialist with over 27 years of experience in the Global furnished housing industry, servicing the Greater Los Angeles area. Specializing in “warm environments” we offer a customized approach to satisfying our guests and client’s needs by offering a wide array of options in highly desirable areas. Additionally, Lantern Dwelling Partners offers assistance and expertise to home buyers, sellers and investors.

Industry/Entity Type

Real Estate

Number of Pages Required

1 page

Font styles to use
Serif
Sans Serif
Decorative

```html
<!DOCTYPE html>
<html lang="en">
<head>
<meta charset="utf-8">
<title>Lantern Dwelling Partners</title>
<link rel="stylesheet" href="https://fonts.googleapis.com/css2?family=Open+Sans:wght@400;600;700&family=Roboto+Slab:wght@400;700&display=swap">
<style>
:root{
  --teal:#0b9a7c;
  --teal-dark:#08856b;
  --lime:#8dc63f;
  --slate:#3f454b;
  --mist:#e9ebee;
  --ink:#333a40;
  --footer:#22262b;
  --footer-deep:#1a1d21;
  --white:#ffffff;
}
*{box-sizing:border-box;margin:0;padding:0}
html,body{width:1200px;height:2782px;overflow:hidden}
body{position:relative;font-family:"Open Sans",Arial,sans-serif;color:var(--ink);background:var(--white)}
.abs{position:absolute}
.serif{font-family:"Roboto Slab",Georgia,serif}

/* hero */
.hero{left:0;top:0;width:1200px;height:543px;background:linear-gradient(180deg,#7fa7c4 0%,#9bb4c2 30%,#56604f 62%,#3a4a2c 100%)}
.hero-house{left:300px;top:40px;width:780px;height:400px;background:linear-gradient(135deg,#d9dbd6 0%,#9a9a94 45%,#5c5d58 100%);opacity:.8}
.topbar{left:117px;top:8px;width:966px;font-size:13px;color:var(--white);display:flex;justify-content:space-between;align-items:center}
.topbar .contact{display:flex;align-items:center;gap:10px}
.social{display:flex;gap:5px}
.social span{width:16px;height:16px;background:var(--lime);display:block}
.logo{left:117px;top:33px;width:230px;height:65px;background:var(--white);display:flex;flex-direction:column;justify-content:center;padding-left:18px}
.logo .name{font-family:"Open Sans",sans-serif;font-weight:700;color:var(--teal);font-size:19px;line-height:1.15}
.nav{left:347px;top:33px;width:736px;height:65px;background:var(--lime);display:flex;align-items:center;padding-left:10px}
.nav a{color:var(--white);text-decoration:none;font-family:"Roboto Slab",Georgia,serif;font-size:13px;padding:0 18px;height:65px;display:flex;align-items:center}
.nav a.current{background:rgba(255,255,255,.18)}
.tagline{left:117px;height:38px;background:var(--teal);color:var(--white);font-weight:700;font-size:22px;line-height:38px;padding:0 12px;letter-spacing:.3px}
.slider-dots{left:1034px;top:407px;display:flex;gap:4px}
.slider-dots span{width:11px;height:11px;background:#dfe3e5;display:block}
.slider-dots span.on{background:var(--teal)}
.search{left:117px;top:445px;width:966px;height:98px;background:rgba(40,44,46,.88)}
.search-title{left:18px;top:14px;font-family:"Roboto Slab",Georgia,serif;color:var(--lime);font-size:15px;font-weight:700}
.field{top:46px;height:30px;background:var(--white);font-size:12px;color:#666;line-height:30px;padding-left:10px}
.field .caret{position:absolute;right:10px;top:13px;border:4px solid transparent;border-top-color:#999}
.btn-search{top:46px;left:796px;width:152px;height:30px;background:var(--lime);color:var(--white);font-weight:700;font-size:13px;text-align:center;line-height:30px}

/* shared */
.section-title{width:1200px;left:0;text-align:center;font-family:"Roboto Slab",Georgia,serif;color:var(--teal);font-size:25px}
.lead{left:210px;width:780px;text-align:center;font-size:12px;line-height:24px;color:#444}
.btn{height:28px;display:flex;font-size:12px;color:var(--white)}
.btn .label{background:var(--teal);padding:0 15px;line-height:28px}
.btn .go{width:26px;background:var(--lime);display:flex;align-items:center;justify-content:center}

/* welcome */
.welcome{left:0;top:543px;width:1200px;height:284px;background:var(--mist)}

/* property grid */
.grid{left:117px;top:985px;width:966px;height:410px;display:grid;grid-template-columns:repeat(4,1fr);grid-template-rows:repeat(2,1fr)}
.photo{width:100%;height:100%}
.card{position:relative;padding:16px 18px;font-size:12px}
.card.dark{background:var(--slate);color:var(--white)}
.card.light{background:var(--mist);color:#555}
.card h3{font-family:"Roboto Slab",Georgia,serif;font-weight:400;font-size:17px}
.card.light h3{color:#555}
.price-row{display:flex;align-items:center;gap:14px;margin-top:16px}
.price{color:var(--lime);font-weight:700;font-size:15px}
.tag{background:var(--slate);color:var(--white);font-size:10px;padding:3px 10px 3px 14px;clip-path:polygon(8px 0,100% 0,100% 100%,8px 100%,0 50%)}
.card.dark .tag{background:var(--white);color:var(--slate)}
.specs{display:grid;grid-template-columns:1fr 1fr;row-gap:16px;margin-top:14px}
.spec{display:flex;gap:8px}
.spec svg{flex:none;margin-top:4px}
.spec small{display:block;font-size:11px}
.spec b{font-weight:400;font-size:18px;line-height:1.1}
.spec b i{font-style:normal;font-size:11px}
.arrow{width:26px;height:26px;background:#eceef0;display:flex;align-items:center;justify-content:center}

/* info split */
.info{top:1452px;width:600px;height:358px;color:var(--white);padding:46px 0 0 117px}
.info.buyer{left:0;background:linear-gradient(120deg,#0c8a6f,#0b9a7c 60%,#139b80)}
.info.seller{left:600px;background:linear-gradient(120deg,#86c13a,#8dc63f 60%,#97cd4c);padding-left:117px}
.info h2{font-family:"Roboto Slab",Georgia,serif;font-weight:400;font-size:25px;margin-bottom:14px}
.info p{font-size:12px;line-height:22px;width:370px;margin-bottom:10px}

/* testimonial */
.testimonial{left:0;top:1810px;width:1200px;height:282px;background:var(--mist)}
.quote-mark{font-family:"Roboto Slab",Georgia,serif;font-size:60px;color:#c4c8cc;line-height:1}
.tdots{left:576px;top:2036px;display:flex;gap:5px}
.tdots span{width:11px;height:11px;border-radius:50%;background:#c9ccd0;display:block}
.tdots span.on{background:var(--lime)}

/* news */
.news-item h4{font-family:"Roboto Slab",Georgia,serif;font-size:14px;color:#222;line-height:21px;font-weight:700;width:290px}
.news-item .date{font-size:11px;color:#777;margin:2px 0 8px}
.news-item p{font-size:11.5px;line-height:20px;color:#444;width:290px}
.news-item .more{font-size:11px;color:#555;margin-top:4px;display:flex;align-items:center;gap:6px}

/* footer */
.footer{left:0;top:2473px;width:1200px;height:258px;background:var(--footer);color:#c9ccd0;font-size:11.5px}
.footer h5{font-family:"Roboto Slab",Georgia,serif;font-weight:400;color:var(--lime);font-size:16px;margin-bottom:16px}
.footer ul{list-style:none;line-height:21px}
.footer-bottom{left:0;top:2731px;width:1200px;height:51px;background:var(--footer-deep);color:#c9ccd0;font-size:11px}
</style>
</head>
<body>

<!-- hero -->
<div class="abs hero" role="img" aria-label="Modern white villa with palm trees under a blue sky"></div>
<div class="abs hero-house" role="img" aria-label="Facade of a contemporary house with stone wall and glass"></div>

<div class="abs topbar">
  <span>Phone: (555) 014 2286</span>
  <span class="contact">Email: info@lanterndwelling.example <span style="opacity:.6">|</span>
    <span class="social"><span></span><span></span><span></span><span></span></span>
  </span>
</div>

<div class="abs logo"><span class="name">Lantern Dwelling<br>Partners</span></div>
<nav class="abs nav">
  <a class="current">HOME</a><a>ABOUT US</a><a>PROPERTY</a><a>BUYER INFO</a><a>SELLER INFO</a><a>NEWS</a><a>CONTACT US</a>
</nav>

<div class="abs tagline" style="top:256px">WE ARE SERVICING THE GREATER</div>
<div class="abs tagline" style="top:300px">LOS ANGELES AREA</div>
<div class="abs slider-dots"><span class="on"></span><span></span><span></span></div>

<div class="abs search">
  <div class="abs search-title">SEARCH PROPERTY</div>
  <div class="abs field" style="left:18px;width:288px">Select Location<span class="caret"></span></div>
  <div class="abs field" style="left:328px;width:111px">Min Price</div>
  <div class="abs field" style="left:451px;width:113px">Max Price</div>
  <div class="abs field" style="left:580px;width:88px">Bed<span class="caret"></span></div>
  <div class="abs field" style="left:675px;width:87px">Bath<span class="caret"></span></div>
  <div class="abs btn-search">Property Search</div>
</div>

<!-- welcome -->
<section class="abs welcome"></section>
<div class="abs section-title" style="top:572px;font-size:15px;color:#333">WELCOME TO</div>
<div class="abs section-title" style="top:592px">LANTERN DWELLING PARTNERS</div>
<p class="abs lead" style="left:145px;width:910px;top:640px">Lorem Ipsum is simply dummy text of the printing and typesetting industry. Lorem Ipsum has been the industry's standard dummy text ever since the 1500s, when an unknown printer took a galley of type and scrambled it to make a type specimen book. It has survived not only five centuries, but also the leap into electronic typesetting, remaining essentially unchanged. It was popularised in the 1960s with the release of printed sheets containing Lorem Ipsum passages, and more recently with desktop publishing software like modern layout editors including versions of Lorem Ipsum.</p>
<div class="abs btn" style="left:542px;top:764px"><span class="label">Learn More</span><span class="go"><svg width="8" height="10"><path d="M1 1l5 4-5 4" stroke="#fff" stroke-width="2" fill="none"/></svg></span></div>

<!-- recent property -->
<div class="abs section-title" style="top:855px">RECENT PROPERTY</div>
<p class="abs lead" style="top:892px">Lorem Ipsum is simply dummy text of the printing and typesetting industry. Lorem Ipsum has been the industry's standard dummy text ever since the 1500s, when an unknown printer took a galley of type and scrambled it to make a type specimen book.</p>

<div class="abs arrow" style="left:44px;top:1176px"><svg width="8" height="10"><path d="M6 1L2 5l4 4" stroke="#333" stroke-width="2" fill="none"/></svg></div>
<div class="abs arrow" style="left:1128px;top:1176px"><svg width="8" height="10"><path d="M2 1l4 4-4 4" stroke="#333" stroke-width="2" fill="none"/></svg></div>

<div class="abs grid">
  <div class="photo" role="img" aria-label="White modern villa beside a lawn" style="background:linear-gradient(135deg,#e7eae6,#9fb08a 60%,#4f7a36)"></div>
  <div class="card dark">
    <h3>Villa in Coral Gables</h3>
    <div class="price-row"><span class="price">$825,000</span><span class="tag">FOR SALE</span></div>
    <div class="specs">
      <div class="spec"><svg width="18" height="16"><rect x="1" y="1" width="16" height="14" fill="none" stroke="#0b9a7c" stroke-width="2"/></svg><div><small>Area</small><b>3500<i>Sq Ft</i></b></div></div>
      <div class="spec"><svg width="18" height="16"><path d="M1 15V5h16v10M1 11h16" stroke="#0b9a7c" stroke-width="2" fill="none"/></svg><div><small>Bedrooms</small><b>03</b></div></div>
      <div class="spec"><svg width="18" height="16"><path d="M1 8h16v3a4 4 0 0 1-4 4H5a4 4 0 0 1-4-4z" fill="#0b9a7c"/></svg><div><small>Bathrooms</small><b>02</b></div></div>
      <div class="spec"><svg width="18" height="16"><path d="M1 15V6l8-5 8 5v9H1zM5 9h8v6H5z" fill="#0b9a7c"/></svg><div><small>Garages</small><b>01</b></div></div>
    </div>
  </div>
  <div class="photo" role="img" aria-label="Contemporary house lit at dusk beside a pool" style="background:linear-gradient(160deg,#a4b3d4,#6f7fa8 50%,#2f3a55)"></div>
  <div class="card light">
    <h3>Villa in Coral Gables</h3>
    <div class="price-row"><span class="price">$825,000</span><span class="tag">FOR SALE</span></div>
    <div class="specs">
      <div class="spec"><svg width="18" height="16"><rect x="1" y="1" width="16" height="14" fill="none" stroke="#0b9a7c" stroke-width="2"/></svg><div><small>Area</small><b>3500<i>Sq Ft</i></b></div></div>
      <div class="spec"><svg width="18" height="16"><path d="M1 15V5h16v10M1 11h16" stroke="#0b9a7c" stroke-width="2" fill="none"/></svg><div><small>Bedrooms</small><b>03</b></div></div>
      <div class="spec"><svg width="18" height="16"><path d="M1 8h16v3a4 4 0 0 1-4 4H5a4 4 0 0 1-4-4z" fill="#0b9a7c"/></svg><div><small>Bathrooms</small><b>02</b></div></div>
      <div class="spec"><svg width="18" height="16"><path d="M1 15V6l8-5 8 5v9H1zM5 9h8v6H5z" fill="#0b9a7c"/></svg><div><small>Garages</small><b>01</b></div></div>
    </div>
  </div>
  <div class="card light">
    <h3>Villa in Coral Gables</h3>
    <div class="price-row"><span class="price">$825,000</span><span class="tag">FOR SALE</span></div>
    <div class="specs">
      <div class="spec"><svg width="18" height="16"><rect x="1" y="1" width="16" height="14" fill="none" stroke="#0b9a7c" stroke-width="2"/></svg><div><small>Area</small><b>3500<i>Sq Ft</i></b></div></div>
      <div class="spec"><svg width="18" height="16"><path d="M1 15V5h16v10M1 11h16" stroke="#0b9a7c" stroke-width="2" fill="none"/></svg><div><small>Bedrooms</small><b>03</b></div></div>
      <div class="spec"><svg width="18" height="16"><path d="M1 8h16v3a4 4 0 0 1-4 4H5a4 4 0 0 1-4-4z" fill="#0b9a7c"/></svg><div><small>Bathrooms</small><b>02</b></div></div>
      <div class="spec"><svg width="18" height="16"><path d="M1 15V6l8-5 8 5v9H1zM5 9h8v6H5z" fill="#0b9a7c"/></svg><div><small>Garages</small><b>01</b></div></div>
    </div>
  </div>
  <div class="photo" role="img" aria-label="Two-storey suburban family house with lawn" style="background:linear-gradient(170deg,#8fb2d8,#c7c9c8 45%,#6d7a66 75%,#4c7a34)"></div>
  <div class="card dark">
    <h3>Villa in Coral Gables</h3>
    <div class="price-row"><span class="price">$825,000</span><span class="tag">FOR SALE</span></div>
    <div class="specs">
      <div class="spec"><svg width="18" height="16"><rect x="1" y="1" width="16" height="14" fill="none" stroke="#0b9a7c" stroke-width="2"/></svg><div><small>Area</small><b>3500<i>Sq Ft</i></b></div></div>
      <div class="spec"><svg width="18" height="16"><path d="M1 15V5h16v10M1 11h16" stroke="#0b9a7c" stroke-width="2" fill="none"/></svg><div><small>Bedrooms</small><b>03</b></div></div>
      <div class="spec"><svg width="18" height="16"><path d="M1 8h16v3a4 4 0 0 1-4 4H5a4 4 0 0 1-4-4z" fill="#0b9a7c"/></svg><div><small>Bathrooms</small><b>02</b></div></div>
      <div class="spec"><svg width="18" height="16"><path d="M1 15V6l8-5 8 5v9H1zM5 9h8v6H5z" fill="#0b9a7c"/></svg><div><small>Garages</small><b>01</b></div></div>
    </div>
  </div>
  <div class="photo" role="img" aria-label="Beige traditional house with front garden" style="background:linear-gradient(170deg,#a9c3dc,#c9b98e 45%,#8d8460 70%,#4a7a2e)"></div>
</div>

<!-- buyer / seller -->
<section class="abs info buyer" role="img" aria-label="Teal-tinted photo of happy home buyers">
  <h2>BUYER INFO</h2>
  <p>Lorem Ipsum is simply dummy text of the printing and typesetting industry. Lorem Ipsum has been the industry's standard dummy text ever since the 1500s, when an unknown printer took a galley of type and scrambled it to make a type specimen book.</p>
  <p>It has survived not only five centuries, but also the leap into electronic typesetting, remaining essentially unchanged. It was popularised in the 1960s with the release of printed sheets containing.</p>
  <div class="btn" style="margin-top:14px"><span class="label" style="background:var(--teal-dark)">Learn More</span><span class="go"><svg width="8" height="10"><path d="M1 1l5 4-5 4" stroke="#fff" stroke-width="2" fill="none"/></svg></span></div>
</section>
<section class="abs info seller" role="img" aria-label="Green-tinted photo of a smiling couple selling their home">
  <h2>SELLER INFO</h2>
  <p>Lorem Ipsum is simply dummy text of the printing and typesetting industry. Lorem Ipsum has been the industry's standard dummy text ever since the 1500s, when an unknown printer took a galley of type and scrambled it to make a type specimen book.</p>
  <p>It has survived not only five centuries, but also the leap into electronic typesetting, remaining essentially unchanged. It was popularised in the 1960s with the release of printed sheets containing.</p>
  <div class="btn" style="margin-top:14px"><span class="label">Learn More</span><span class="go" style="background:#a6d35f"><svg width="8" height="10"><path d="M1 1l5 4-5 4" stroke="#fff" stroke-width="2" fill="none"/></svg></span></div>
</section>

<!-- testimonial -->
<section class="abs testimonial"></section>
<div class="abs section-title" style="top:1842px">WHAT OUR CLIENTS SAY</div>
<div class="abs quote-mark" style="left:115px;top:1915px">&ldquo;</div>
<div class="abs" role="img" aria-label="Client portrait" style="left:160px;top:1922px;width:96px;height:96px;border-radius:50%;border:3px solid #fff;background:linear-gradient(160deg,#d8d6d2,#a99a8a)"></div>
<div class="abs" style="left:297px;top:1920px;width:2px;height:92px;background:#c9ccd0"></div>
<p class="abs" style="left:334px;top:1918px;width:706px;font-size:12px;line-height:24px;color:#444">Lorem Ipsum is simply dummy text of the printing and typesetting industry. Lorem Ipsum has been the industry's standard dummy text ever since the 1500s, when an unknown printer took a galley of type and scrambled it to make a type specimen book. It has survived not only five centuries...</p>
<div class="abs serif" style="left:334px;top:1994px;color:var(--teal);font-size:17px">Marcus Ellery</div>
<div class="abs quote-mark" style="left:1055px;top:1990px">&rdquo;</div>
<div class="abs tdots"><span class="on"></span><span></span><span></span></div>

<!-- news -->
<div class="abs section-title" style="top:2118px">LATEST NEWS</div>
<div class="abs" style="left:0;width:1200px;top:2158px;text-align:center;font-size:12px;color:#333">Fresh news and Blog from the world of information</div>

<div class="abs" role="img" aria-label="Bright modern living room interior" style="left:117px;top:2224px;width:148px;height:152px;background:linear-gradient(150deg,#f1efea,#c8bfb2 55%,#7d6b58)"></div>
<div class="abs news-item" style="left:288px;top:2218px">
  <h4>Lorem Ipsum is simply dummy text of the and typesetting industry.</h4>
  <div class="date">October 06, 2015</div>
  <p>Lorem Ipsum has been the industry's standard dummy text ever since the 1500s, when an unknown in printer took a galley of type...</p>
  <div class="more"><svg width="12" height="12"><circle cx="6" cy="6" r="5" fill="none" stroke="#8dc63f"/><path d="M5 3.5L7.5 6 5 8.5" stroke="#8dc63f" fill="none"/></svg>Read More</div>
</div>
<div class="abs" role="img" aria-label="Hand holding keys with a small model house" style="left:620px;top:2224px;width:148px;height:152px;background:linear-gradient(150deg,#f4f4f4,#d9c2b5 55%,#b0463a)"></div>
<div class="abs news-item" style="left:790px;top:2218px">
  <h4>Lorem Ipsum is simply dummy text of the and typesetting industry.</h4>
  <div class="date">October 06, 2015</div>
  <p>Lorem Ipsum has been the industry's standard dummy text ever since the 1500s, when an unknown in printer took a galley of type...</p>
  <div class="more"><svg width="12" height="12"><circle cx="6" cy="6" r="5" fill="none" stroke="#8dc63f"/><path d="M5 3.5L7.5 6 5 8.5" stroke="#8dc63f" fill="none"/></svg>Read More</div>
</div>
<div class="abs btn" style="left:542px;top:2408px"><span class="label">View More</span><span class="go"><svg width="8" height="10"><path d="M1 1l5 4-5 4" stroke="#fff" stroke-width="2" fill="none"/></svg></span></div>

<!-- footer -->
<footer class="abs footer">
  <div class="abs" style="left:117px;top:38px">
    <h5>Site Map</h5>
    <ul><li>- About Us</li><li>- Property</li><li>- Buyer Info</li><li>- Seller Info</li><li>- News</li><li>- Contact Us</li></ul>
  </div>
  <div class="abs" style="left:286px;top:38px;width:185px">
    <h5>Newsletter</h5>
    <p style="line-height:20px">Simply dummy text of the printing and typesetting industry.</p>
    <div style="margin-top:12px;width:172px;height:30px;background:#3a3f45;line-height:30px;padding-left:10px;color:#ddd">Enter Email</div>
    <div style="margin-top:12px;width:80px;height:26px;background:var(--lime);color:#fff;font-weight:700;text-align:center;line-height:26px">SUBMIT</div>
  </div>
  <div class="abs" style="left:545px;top:38px;width:230px;line-height:20px">
    <h5>Contact Detail</h5>
    <div style="font-weight:700;color:#fff">LANTERN DWELLING PARTNERS</div>
    <div>1234 Street Name, City Name,<br>United States</div>
    <div style="margin-top:10px">Phone : 555 014 2286</div>
    <div style="margin-top:10px">Email : info@lanterndwelling.example</div>
  </div>
  <div class="abs" role="img" aria-label="Street map showing the office location" style="left:792px;top:42px;width:291px;height:153px;background:linear-gradient(135deg,#d9e7c6,#eef0e6 50%,#bcd9e6)"></div>
  <svg class="abs" style="left:878px;top:90px" width="28" height="36"><path d="M14 35C14 35 26 20 26 12A12 12 0 0 0 2 12C2 20 14 35 14 35z" fill="#0b9a7c"/><circle cx="14" cy="12" r="5" fill="#fff"/></svg>
  <div class="abs" style="left:792px;top:202px">View Map</div>
</footer>
<div class="abs footer-bottom">
  <div class="abs" style="left:117px;top:18px">Terms of Use &nbsp; | &nbsp; Privacy</div>
  <div class="abs" style="left:0;width:1200px;top:18px;text-align:center">Copyright © 2016 - Lantern Dwelling Partners &nbsp;|&nbsp; All Rights Reserved.</div>
  <div class="abs" style="left:977px;top:16px;display:flex;gap:8px">
    <span style="width:18px;height:18px;border-radius:50%;background:#4a5057;display:block"></span>
    <span style="width:18px;height:18px;border-radius:50%;background:#4a5057;display:block"></span>
    <span style="width:18px;height:18px;border-radius:50%;background:#4a5057;display:block"></span>
    <span style="width:18px;height:18px;border-radius:50%;background:#4a5057;display:block"></span>
  </div>
</div>

</body>
</html>
```